依頼詳細
2024年の年賀状のデザインをお願いします(裏面のみ)。

明るく元気で遊び心のあるデザインを希望します。
添付の当社ロゴを一部(どれでもOK)をお使い下さい。
ポイント的に使っていただいても、ロゴ自体を強調していただいてもどちらでも構いません。
干支的要素を入れていただいてもなくてもどちらでも構いません。

HP: http://www.moru-works.co.jp/

※昨年度までもツクバーの方にデザインしていただいています。
ご応募いただいた作品はこちらです。

2014年
http://www.tsukuba-hub.jp/work/detail/510327

2015年
http://www.tsukuba-hub.jp/work/detail/630418

2016年
http://www.tsukuba-hub.jp/work/detail/920461

2017年
http://www.tsukuba-hub.jp/work/detail/1490356

2018年
https://www.tsukuba-hub.jp/work/detail/1860542

2019年
https://www.tsukuba-hub.jp/work/detail/2470193

2020年
https://www.tsukuba-hub.jp/work/detail/2950684

2021年
https://www.tsukuba-hub.jp/work/detail/3580427

2022年
https://www.tsukuba-hub.jp/work/detail/3920175

2023年
https://www.tsukuba-hub.jp/work/detail/4610238
記載項目
1.MRWのロゴ

※MRWの文字は添付ロゴデータから切り貼りしてお使い下さい。
※MRWの文字はデザインの一部として織り込んで下さい。

2.テキスト

明けましておめでとうございます。
本年も変わらぬお引き立てのほど宜しくお願い申し上げます。

〒104-0038 東京都中央区新富町2-318 新富町桜葉ビルディング
TEL:03-5914-2730

※すっきりと見やすいテキストレイアウトをお願いします。
希望イメージ
シンプル 複雑
単色 カラフル
暗い 明るい
日常 高級
遊び心 厳粛
未来的 伝統的
女性的 男性的
納品ファイル
• 高解像度JPG (.jpg)
• イラストレーター形式 (.ai)
補足説明
添付のロゴデータを一部、織り込んで下さい。
■ 選んだ理由

力作揃いで今年も社内で票が割れました。ほぼ横並びの中で、社長の推しを当選作として選ばせていただきました。
(次点には、最後まで競り合った候補作を選ばせていただきました)

■ 提案者全員のお礼・コメント

今年もたくさんご応募をありがとうございました。
ここ数年で一番多いご応募をいただき、嬉しい悲鳴の中、役員と選定を進めさせていただきました。
ストレートなデザインからヒネったもの、題材も竜や龍からタツノオトシゴまで、みなさまの創意工夫には驚かされることが多いです。

こんなご時世で、この先どうなるかは分かりませんが、来年もできればお願いすると思いますので、ご提案いただければ幸いです。
みなさま、良いお年をお迎えください。

```html
<!DOCTYPE html>
<html lang="ja">
<head>
<meta charset="utf-8">
<title>MRW 2024 年賀状</title>
<link href="https://fonts.googleapis.com/css2?family=Noto+Sans+JP:wght@400;500;700;900&display=swap" rel="stylesheet">
<style>
  :root {
    --card-yellow: #f7d81c;
    --circle-white: #ffffff;
    --ink: #1a1a1a;
    --silhouette: #151515;
  }
  html, body {
    margin: 0;
    padding: 0;
    overflow: hidden;
    background: #ffffff;
  }
  .card {
    position: relative;
    width: 813px;
    height: 1200px;
    background: var(--card-yellow);
    overflow: hidden;
    font-family: "Noto Sans JP", sans-serif;
    color: var(--ink);
  }
  .sun-circle {
    position: absolute;
    left: 108px;
    top: 322px;
    width: 600px;
    height: 600px;
    border-radius: 50%;
    background: var(--circle-white);
  }
  .dragon-art {
    position: absolute;
    right: 0;
    top: 0;
    width: 420px;
    height: 520px;
  }
  .lion-art {
    position: absolute;
    left: 0;
    bottom: 0;
    width: 176px;
    height: 280px;
  }
  .greeting {
    position: absolute;
    left: 0;
    width: 813px;
    top: 334px;
    text-align: center;
  }
  .greeting-title {
    margin: 0;
    font-weight: 700;
    font-size: 52px;
    line-height: 68px;
    letter-spacing: 1px;
  }
  .greeting-message {
    margin: 36px 0 0;
    font-weight: 400;
    font-size: 16px;
    letter-spacing: 0.3px;
  }
  .greeting-year {
    margin: 24px 0 0;
    font-weight: 700;
    font-size: 34px;
    line-height: 1.2;
    letter-spacing: 1px;
  }
  .company-name {
    margin: 26px 0 0;
    font-weight: 700;
    font-size: 62px;
    letter-spacing: 10px;
    line-height: 1;
  }
  .company-info {
    position: absolute;
    left: 0;
    width: 813px;
    top: 968px;
    text-align: center;
    font-size: 17px;
    line-height: 30px;
    font-weight: 500;
  }
  .company-info p { margin: 0; }
</style>
</head>
<body>
<div class="card">
  <div class="sun-circle"></div>

  <svg class="dragon-art" viewBox="0 0 420 520" role="img" aria-label="龍のシルエットイラスト(右上から顔を出す黒い龍)">
    <path fill="var(--silhouette)" d="M420 0 L420 300 C390 320 370 380 350 515 C325 470 300 425 268 385 C235 350 205 310 195 270 C150 255 120 225 100 195 C70 165 45 130 25 100 C75 110 125 80 165 40 C190 15 205 0 225 0 Z"/>
  </svg>

  <svg class="lion-art" viewBox="0 0 176 280" role="img" aria-label="獅子舞のシルエットイラスト">
    <path fill="var(--silhouette)" d="M0 20 C60 0 135 30 165 95 C180 145 165 210 135 280 L0 280 Z"/>
  </svg>

  <div class="greeting">
    <h1 class="greeting-title">明けまして<br>おめでとう<br>ございます</h1>
    <p class="greeting-message">本年も変わらぬお引き立てのほど宜しくお願い申し上げます。</p>
    <p class="greeting-year">2024</p>
    <p class="company-name">MRW</p>
  </div>

  <div class="company-info">
    <p>〒104-0038</p>
    <p>東京都中央区新富町2-318</p>
    <p>新富町桜葉ビルディング</p>
    <p>TEL：03-5914-2730</p>
    <p>HP: http://www.moru-works.co.jp/</p>
  </div>
</div>
</body>
</html>
```